Velmint website

A clean uncluttered design that shows at glance that we are in the Media and design and publishing business.

We would like to see designs that use colours that show warmth and quality.

The website should show:
- products
- projects

These should be displaxed in spaces that we can add or interchanges with new products or projects.
Updates

Target Market(s)

Business and project managers and buyers and authors.

Industry/Entity Type

Business

Requirements
Must have
• Good colours. Not too strong, not weak, but reflecting quality.

```html
<!DOCTYPE html>
<html lang="en">
<head>
<meta charset="utf-8">
<title>Velmint Media</title>
<link href="https://fonts.googleapis.com/css2?family=Open+Sans:ital,wght@0,400;0,600;0,700;1,400&display=swap" rel="stylesheet">
<style>
:root{
  --red:#d0140a;
  --red-dark:#6e0c06;
  --cyan:#12afcb;
  --cyan-line:#3dc2da;
  --blue:#1a9fe0;
  --ink:#111;
  --text:#222;
  --grey:#9a9a9a;
  --panel:#fff;
  --shadow:0 1px 4px rgba(0,0,0,.18);
}
*{box-sizing:border-box;margin:0;padding:0}
html,body{width:1012px;height:1200px;overflow:hidden;background:#fff;font-family:"Open Sans",Arial,sans-serif;color:var(--text)}
.page{position:relative;width:1012px;height:1200px}
.topbar{position:absolute;left:0;top:0;width:100%;height:14px;background:var(--red-dark);color:#e8b8b4;font-size:8px;line-height:14px}
.topbar .cert{position:absolute;left:73px}
.topbar .links{position:absolute;right:72px;color:#fff;word-spacing:8px;font-size:9px}
.header{position:absolute;left:0;top:14px;width:100%;height:94px;background:var(--red);color:#fff}
.brand{position:absolute;left:70px;top:24px;display:flex;align-items:center;gap:12px}
.brand .mark{width:22px;height:22px;background:#fff}
.brand .name{font-size:20px;font-weight:700;line-height:20px;letter-spacing:.5px}
.callline{position:absolute;left:596px;top:17px;width:172px;font-size:13px;font-weight:600;letter-spacing:-.4px;white-space:nowrap;display:flex;align-items:center;gap:4px}
.search{position:absolute;left:777px;top:15px;width:163px;height:20px;background:#fff;border-radius:2px;font-size:8px;color:#888;line-height:20px;padding-left:10px}
.search svg{position:absolute;right:7px;top:6px}
.nav{position:absolute;right:72px;top:48px;display:flex;gap:17px;font-size:13px}
.nav .active{border-bottom:2px solid #fff;padding-bottom:1px}
.intro{position:absolute;left:0;top:138px;width:100%;text-align:center}
.intro h1{font-size:29px;font-weight:700;letter-spacing:-1px;color:var(--ink)}
.intro p{width:750px;margin:8px auto 0;font-size:13px;line-height:16px;color:#222}
.intro a{color:var(--red);text-decoration:none}
.sidebar{position:absolute;left:70px;top:278px;width:139px;height:584px;background:var(--cyan)}
.sidebar h2{height:36px;background:var(--red);color:#fff;font-size:12px;font-weight:600;line-height:36px;padding-left:14px}
.sidebar ul{list-style:none}
.sidebar li{color:#fff;font-size:9.5px;line-height:13px;padding:7px 6px 6px 27px;border-bottom:1px solid var(--cyan-line);position:relative}
.sidebar li::before{content:"";position:absolute;left:16px;top:10px;width:6px;height:7px;background:#fff;border-radius:0 4px 4px 0}
.sidebar li.hl{background:#28bcd6}
.sidebar .more{position:absolute;left:50px;bottom:0}
.products{position:absolute;left:217px;top:278px;width:723px;height:300px;background:var(--panel);box-shadow:var(--shadow);overflow:hidden}
.ribbon{position:absolute;left:0;top:0}
.item{position:absolute;top:0;width:194px;height:300px;text-align:center;font-size:13px;line-height:16px}
.item .img{position:absolute;left:22px;width:150px;height:120px;border-radius:6px}
.item .label{position:absolute;left:0;width:100%;top:230px}
.item.sel{border:2px solid #49bfe6}
.item.sel .label{color:var(--red);top:228px}
.arrow{position:absolute}
.box{position:absolute;top:602px;width:230px;height:260px;background:var(--panel);box-shadow:var(--shadow);overflow:hidden}
.app .img{position:absolute;left:18px;top:32px;width:196px;height:120px;background:linear-gradient(#e9e9e9,#c9c9c9);border-radius:4px}
.app h3{position:absolute;top:162px;width:100%;text-align:center;font-size:17px;font-weight:400;color:#111}
.app p{position:absolute;top:188px;left:16px;width:198px;text-align:center;font-size:11px;line-height:13px;color:#222}
.call .img{position:absolute;left:0;top:0;width:230px;height:160px;background:linear-gradient(135deg,#c8d8e6,#9fb5c8 55%,#e5edf3)}
.call .t{position:absolute;left:19px;top:170px;font-size:11px;font-weight:600;color:#222}
.call .num{position:absolute;left:19px;top:188px;font-size:20px;color:var(--cyan);display:flex;align-items:center;gap:4px;white-space:nowrap}
.call .mail{position:absolute;left:21px;top:217px;font-size:17px;color:#aaa;letter-spacing:-.5px;white-space:nowrap}
.quote .tab{position:absolute;right:0;top:0}
.quote .avatar{position:absolute;left:22px;top:24px;width:68px;height:65px;background:linear-gradient(#b8cde0,#8aa6bf)}
.quote .who{position:absolute;left:102px;top:30px}
.quote .who b{display:block;font-size:16px;font-weight:600;color:var(--blue);letter-spacing:-.5px}
.quote .who span{display:block;font-size:10px;line-height:15px;color:#aaa;letter-spacing:-.3px}
.quote .qm{position:absolute;font-size:28px;color:#777;font-weight:700;line-height:1}
.quote p{position:absolute;left:48px;top:110px;width:168px;font-style:italic;font-size:10.5px;line-height:13px;color:#333}
.projhead{position:absolute;left:388px;top:886px;width:250px;height:32px}
.projhead .line{position:absolute;top:15px;left:0;width:250px;height:1px;background:var(--red)}
.projhead .pill{position:absolute;left:66px;top:0;width:119px;height:32px;background:var(--red);border-radius:16px;color:#fff;font-size:14px;font-weight:600;text-align:center;line-height:32px}
.projects{position:absolute;left:70px;top:950px;display:flex;gap:4.3px}
.proj{width:93px;text-align:center;font-size:10.5px;line-height:16px;color:#222}
.proj .img{height:57px;margin-bottom:6px;background:linear-gradient(135deg,#c9c9c9,#8d8d8d)}
.proj.sel .img{border:2px solid #3ab7e6;background:linear-gradient(#3f5a3c,#a7c090)}
.proj.first{font-weight:700}
.footer{position:absolute;left:0;top:1102px;width:100%;height:96px;background:#000;color:#fff;text-align:center}
.footer .links{margin-top:26px;font-size:10.5px;word-spacing:1px}
.footer .copy{margin-top:19px;font-size:10px}
</style>
</head>
<body>
<div class="page">
  <div class="topbar"><span class="cert">Uni En Iso 9001 Certified Company</span><span class="links">ENGLISH LOGIN REGISTER</span></div>
  <header class="header">
    <div class="brand"><span class="mark"></span><span class="name">VELMINT<br>MEDIA</span></div>
    <div class="callline">
      <svg width="12" height="14" viewBox="0 0 12 14"><path d="M3 1l2 3-1.5 1.5c.6 1.8 1.6 3 3.4 4L8.5 8 11 10l-1.5 2.5C5 12 1 8 1 2.5z" fill="#fff"/></svg>
      CALL : +39 0421 77 30 18
    </div>
    <div class="search">Search<svg width="9" height="9" viewBox="0 0 9 9"><circle cx="3.6" cy="3.6" r="2.8" fill="none" stroke="#888" stroke-width="1.2"/><path d="M5.7 5.7L8.5 8.5" stroke="#888" stroke-width="1.3"/></svg></div>
    <nav class="nav"><span>Home</span><span class="active">Products</span><span>Projects</span><span>About us</span><span>Faq</span><span>Contacts</span></nav>
  </header>

  <section class="intro">
    <h1>Lorem ipsum dolor sit amet, consectetur adipiscing elit.</h1>
    <p>Lorem ipsum dolor sit amet, consectetur adipiscing elit. In fermentum dolor non augue pretium egestas. Donec sem eros, tincidunt at congue ut, posuere sit amet est. Vivamus scelerisque viverra odio sit amet laoreet. Ut nec neque non justo rutrum tempor lobortis eu ante. Aliquam sagittis, nibh quis commodo auctor, risus mauris laoreet lectus <a href="#">read more...</a></p>
  </section>

  <aside class="sidebar">
    <h2>Product Categories</h2>
    <ul>
      <li>Velmint Ipsum Name</li>
      <li class="hl">Lorem Ipsum<br>Dummy Title Name</li>
      <li>Lorem Ipsum<br>Dummy Title Name</li>
      <li>Dummy Product</li>
      <li>Dummy Product</li>
      <li>Lorem Ipsum Name</li>
      <li>Lorem Ipsum<br>Dummy Title Name</li>
      <li>Lorem Ipsum<br>Dummy Title Name</li>
      <li>Lorem Ipsum<br>Dummy Title Name<br>Standard Dummy</li>
      <li>Dummy Product</li>
      <li>Lorem Ipsum Name</li>
      <li>Lorem Ipsum<br>Dummy Title Name</li>
      <li>Dummy Product</li>
      <li>Lorem Ipsum Name</li>
      <li>Dummy Product</li>
      <li>Dummy Product</li>
    </ul>
    <svg class="more" width="40" height="14" viewBox="0 0 40 14"><path d="M4 14a16 16 0 0 1 32 0" fill="none" stroke="#fff" stroke-width="1"/><path d="M9 14a11 11 0 0 1 22 0" fill="#fff"/><path d="M17 11l3-3 3 3" fill="none" stroke="#999" stroke-width="1"/></svg>
  </aside>

  <section class="products">
    <svg class="ribbon" width="92" height="92" viewBox="0 0 92 92"><path d="M0 0h92L0 88z" fill="#fff"/><path d="M58 0h34L0 88V58z" fill="#000"/><text x="0" y="0" transform="translate(14 62) rotate(-45)" fill="#fff" font-family="Open Sans, sans-serif" font-size="11" font-weight="600">Our Products</text></svg>
    <div class="item" style="left:64px">
      <div class="img" role="img" aria-label="Black media player box with remote control" style="top:90px;background:linear-gradient(#555,#1d1d1d)"></div>
      <div class="label">Lorem Ipsum<br>Product Name</div>
    </div>
    <div class="item sel" style="left:275px">
      <div class="img" role="img" aria-label="Black studio headphones with microphone" style="top:58px;left:20px;background:linear-gradient(#4a4a4a,#161616)"></div>
      <div class="label">Lorem Ipsum Digital<br>Head Phone</div>
    </div>
    <div class="item" style="left:500px">
      <div class="img" role="img" aria-label="Black slim disc player" style="top:120px;height:60px;background:linear-gradient(#3a3a3a,#0d0d0d)"></div>
      <div class="label">Lorem Ipsum<br>Product Name</div>
    </div>
    <svg class="arrow" style="left:14px;top:128px" width="46" height="46" viewBox="0 0 46 46"><circle cx="23" cy="23" r="22" fill="none" stroke="#7fd6ec"/><circle cx="23" cy="23" r="17" fill="none" stroke="#7fd6ec"/><circle cx="23" cy="23" r="13" fill="#15aee0"/><path d="M25 18l-5 5 5 5" fill="none" stroke="#0b3550" stroke-width="2"/></svg>
    <svg class="arrow" style="left:666px;top:153px" width="46" height="46" viewBox="0 0 46 46"><circle cx="23" cy="23" r="22" fill="none" stroke="#7fd6ec"/><circle cx="23" cy="23" r="17" fill="none" stroke="#7fd6ec"/><circle cx="23" cy="23" r="13" fill="#15aee0"/><path d="M21 18l5 5-5 5" fill="none" stroke="#0b3550" stroke-width="2"/></svg>
  </section>

  <article class="box app" style="left:220px">
    <div class="img" role="img" aria-label="Laptop and phone showing a web shop"></div>
    <h3>APPLICATION</h3>
    <p>Ut nec neque non justo rutrum tempor lobortis eu ante. Aliquam sagittis, nibh quis commodo auctor,</p>
  </article>

  <article class="box call" style="left:465px">
    <div class="img" role="img" aria-label="Smiling businessman holding a laptop in an office"></div>
    <div class="t">CALL US TOLL FREE:</div>
    <div class="num"><svg width="14" height="18" viewBox="0 0 12 14"><path d="M3 1l2 3-1.5 1.5c.6 1.8 1.6 3 3.4 4L8.5 8 11 10l-1.5 2.5C5 12 1 8 1 2.5z" fill="#12afcb"/></svg>+39 0421 77 30 19</div>
    <div class="mail">info@velmintmedia.com</div>
  </article>

  <article class="box quote" style="left:710px">
    <svg class="tab" width="48" height="22" viewBox="0 0 48 22"><path d="M0 0h48v22H14z" fill="#111"/><path d="M27 7l-3 4 3 4M33 7l3 4-3 4" fill="none" stroke="#fff" stroke-width="1.5"/></svg>
    <div class="avatar" role="img" aria-label="Portrait photo of the reviewer"></div>
    <div class="who"><b>Daniel Marsh</b><span>Posted on 01 Jan 2014</span><span>Australia, Sydney</span></div>
    <span class="qm" style="left:22px;top:110px">&ldquo;</span>
    <p>Lorem ipsum dolor sit amet, consectetur adipiscing elit, sed do eiusmod tempor incididunt ut labore et dolore magna aliqua. Ut enim ad minim veniam, quis nostrud exercitation ullamco laboris nisi ut aliquip ex ea commodo consequat. Duis aute irure dolor in reprehenderit in voluptate velit esse</p>
    <span class="qm" style="left:192px;top:228px">&rdquo;</span>
  </article>

  <div class="projhead"><div class="line"></div><div class="pill">Our Projects</div></div>

  <section class="projects">
    <div class="proj first"><div class="img" role="img" aria-label="Hand holding a phone"></div>Lorem Ipsum<br>Product Name</div>
    <div class="proj"><div class="img" role="img" aria-label="Person wearing headphones"></div>Lorem Ipsum<br>Product Name</div>
    <div class="proj sel"><div class="img" role="img" aria-label="Screen with a green display"></div>Lorem Ipsum<br>Product Name</div>
    <div class="proj"><div class="img" role="img" aria-label="Person wearing headphones"></div>Lorem Ipsum<br>Product Name</div>
    <div class="proj"><div class="img" role="img" aria-label="Camera in hand"></div>Lorem Ipsum<br>Product Name</div>
    <div class="proj"><div class="img" role="img" aria-label="Hand using a tablet"></div>Lorem Ipsum<br>Product Name</div>
    <div class="proj"><div class="img" role="img" aria-label="Camera in hand"></div>Lorem Ipsum<br>Product Name</div>
    <div class="proj"><div class="img" role="img" aria-label="Business people in an office"></div>Lorem Ipsum<br>Product Name</div>
    <div class="proj"><div class="img" role="img" aria-label="Hand holding a phone"></div>Lorem Ipsum<br>Product Name</div>
  </section>

  <footer class="footer">
    <div class="links">Home | About | Contact | Site map | Terms | Tel: +39 042177 30 20</div>
    <div class="copy">© 2014</div>
  </footer>
</div>
</body>
</html>
```